Business card for a Exhibition booth fabrication company

Hi. My company would like to change our corporate name card. We are an events and Exhibition stand builder company. We would like our corporate name card to resonate what we do. I need someone to create something unique that relates to the industry that I am in. The graphic designer should be creative to incorporate the elements of my industry and try to blend in well in the design of the card. Our aim is to ensure that we are unique and our card can look different from our competitors.
Updates

The decision maker was very busy and didnt had time to make this decision

Target Market(s)

Marketing and events manager from all companies

Contact Information for Business Card

The business card should have the following details:
Name
Job Title
Email
Website

Colors

Designer to choose colors to be used in the design.

Requirements
Must have
• The card must be look something that is relevant to the service that I am providing. My website is: www.velmora-buildworks.example
• You can see my website to get more information on what service that I am doing
Nice to have
• On the back of my card, I would like to have a globe image with the incorporation of my company logo. This is to indicate that my services can be done in any part of the world.

```html
<!DOCTYPE html>
<html lang="en">
<head>
<meta charset="utf-8">
<title>Velmora Buildworks – Business Card</title>
<link rel="stylesheet" href="https://fonts.googleapis.com/css2?family=Open+Sans:wght@400;600;700&display=swap">
<style>
  :root{
    --stage-light:#dcdddf;
    --stage-dark:#a4a5a8;
    --card-grey:#616264;
    --map-grey:#7c7d80;
    --accent-red:#ec1c24;
    --paper:#ffffff;
    --brand-grey:#6d6e70;
    --brand-silver:#b9babc;
    --ink-light:#ffffff;
  }
  *{box-sizing:border-box;margin:0;padding:0}
  html,body{width:1200px;height:1118px;overflow:hidden}
  body{
    background:linear-gradient(90deg,var(--stage-light) 0%,#c3c4c6 50%,var(--stage-dark) 100%);
    font-family:"Open Sans",Arial,sans-serif;
    position:relative;
  }
  .card{
    position:absolute;left:223px;width:753px;height:443px;
    border-radius:36px;overflow:hidden;background:var(--card-grey);
    color:var(--ink-light);
  }
  .card--front{top:90px}
  .card--back{top:586px}

  .front-swoosh{position:absolute;inset:0;width:100%;height:100%}

  .brand-lockup{
    position:absolute;left:40px;top:226px;
    display:flex;align-items:center;gap:12px;
  }
  .brand-lockup__mark{width:20px;height:20px;background:var(--accent-red)}
  .brand-lockup__name{
    font-size:22px;font-weight:600;letter-spacing:1.8px;color:var(--brand-grey);
  }

  .holder{position:absolute;right:17px;top:56px;text-align:right}
  .holder__name{font-size:17px;font-weight:700;letter-spacing:1px;line-height:1}
  .holder__title{font-size:14px;letter-spacing:1px;margin-top:8px;line-height:1}

  .address{position:absolute;right:17px;top:228px;text-align:right;font-size:17px;line-height:30px}

  .contact-list{position:absolute;right:17px;top:312px;list-style:none}
  .contact-list li{
    display:flex;justify-content:flex-end;align-items:center;gap:12px;
    font-size:17px;height:34px;
  }
  .contact-list svg{width:19px;height:19px;fill:none;stroke:var(--ink-light);stroke-width:1.6}

  .world-map{
    position:absolute;left:0;top:76px;width:100%;height:296px;
    background:radial-gradient(ellipse at 50% 45%,#86878a 0%,var(--map-grey) 55%,rgba(124,125,128,0.6) 100%);
  }
  .back-brand{
    position:absolute;left:0;right:0;top:190px;text-align:center;
    font-size:36px;font-weight:600;letter-spacing:3px;color:var(--brand-silver);
  }
  .back-web{
    position:absolute;left:0;right:0;top:400px;text-align:center;
    font-size:19px;letter-spacing:4.5px;
  }
</style>
</head>
<body>

<section class="card card--front">
  <svg class="front-swoosh" viewBox="0 0 753 443" aria-hidden="true">
    <ellipse cx="180" cy="150" rx="470" ry="250" transform="rotate(-38 180 150)" fill="var(--accent-red)"/>
    <ellipse cx="160" cy="140" rx="445" ry="236" transform="rotate(-38 160 140)" fill="var(--paper)"/>
  </svg>

  <div class="brand-lockup">
    <span class="brand-lockup__mark"></span>
    <span class="brand-lockup__name">VELMORA BUILDWORKS</span>
  </div>

  <div class="holder">
    <p class="holder__name">DANIEL OKAFOR</p>
    <p class="holder__title">PRESIDENT</p>
  </div>

  <p class="address">Street Name, City Name<br>Zipcode - 01234</p>

  <ul class="contact-list">
    <li>012-555-0147
      <svg viewBox="0 0 20 20"><path d="M5 3l3 3-2 2c1 2.5 3.5 5 6 6l2-2 3 3-2 2C9 17 3 11 3 5z" fill="var(--ink-light)" stroke="none"/></svg>
    </li>
    <li>info@velmora-buildworks.example
      <svg viewBox="0 0 20 20"><rect x="2" y="5" width="16" height="11" fill="var(--ink-light)" stroke="none"/><path d="M2 5l8 6 8-6M2 16l6-5M18 16l-6-5" stroke="var(--card-grey)"/></svg>
    </li>
    <li>www.velmora-buildworks.example
      <svg viewBox="0 0 20 20"><circle cx="10" cy="10" r="8"/><ellipse cx="10" cy="10" rx="3.5" ry="8"/><path d="M2 10h16M3.5 6h13M3.5 14h13"/></svg>
    </li>
  </ul>
</section>

<section class="card card--back">
  <div class="world-map" role="img" aria-label="World map silhouette in light grey"></div>
  <p class="back-brand">VELMORA BUILDWORKS</p>
  <p class="back-web">www.velmora-buildworks.example</p>
</section>

</body>
</html>
```